KT Prime Motion personal training needs a new Business Card design for 2016

Business Card design:
Our current business card is very plain
We are bringing on our first team member next year and thought its a perfect time to have a new face lift for our company!

We are a Personal Training business "KT Prime Motion" who specializes in strength and conditioning / weightloss training,
We also run a yearly Bootcamp called "Ferocity Drillcamps", this is our Logo Design which we are looking for

The pink and blue in the logo are our business colours, how ever we don't want those colours to heavily dominate the card.

We are looking for a business card which is eye catching, and creative.

I am open to suggestions and any designs :)

Logo Design:

For our Logo Design we are looking for a bright, energetic logo, preferably a word logo which portrays strength and high intensity
If it has icon's etc in it thats fine again im open for suggestions :)
The Logo Design is for our Bootcamp which runs yearly
The bootcamp is called "Ferocity Drillcamp"

Target Market(s)

Age 20-40
Individuals who want to look great and have more energy

Industry/Entity Type

Business

Contact Information for Business Card

On the front
KT Prime Motion Doriel Maxton Personal Training / Bootcamps / Pilates / Nutrition Healthy mind, Healthy body, Ultimate lifestyle < our slogan
Icons for the following
Email:
Mobile:
Facebook:
Instagram:

On the back we would like to include somewhere
"Show this card to receive 50% off your first 30min pt session"
"Valid to one user only"

Logo Text

Ferocity Drillcamp

Font styles to use
Serif

Colors
e34197
0255a3
000000
ffffff

Requirements
Must have
• - Icons for instagram, facebook, email and mobile phone
• - Slogan: Healthy mind, Healthy body, Ultimate lifestyle
• - What we offer: Personal Training , Bootcamps, Pilates, Nutrition
• - Logo
• -
Nice to have
• - Our 50% offer on the back
• - a place for a photo
Should not have
• - Pink and Blue everywhere

```html
<!DOCTYPE html>
<html lang="en">
<head>
<meta charset="utf-8">
<title>KT Prime Motion – Business Card</title>
<link rel="stylesheet" href="https://fonts.googleapis.com/css2?family=Arimo:wght@400;700&family=Didact+Gothic&display=swap">
<style>
  :root {
    --brand-blue: #0255a3;
    --brand-pink: #e34197;
    --ink: #000000;
    --paper: #ffffff;
    --backdrop: #ecebe8;
    --watermark: rgba(2, 85, 163, 0.06);
  }
  * { box-sizing: border-box; margin: 0; padding: 0; }
  html, body { width: 1189px; height: 1200px; overflow: hidden; }
  body { background: var(--backdrop); position: relative; font-family: "Didact Gothic", sans-serif; color: var(--ink); }

  .card {
    position: absolute; left: 171px; width: 856px; height: 488px;
    background: var(--paper); border-radius: 16px; overflow: hidden;
    box-shadow: 0 2px 6px rgba(0,0,0,0.18);
  }
  .card--offer { top: 67px; }
  .card--contact { top: 626px; }

  /* offer side */
  .offer-watermark {
    position: absolute; left: 208px; top: 19px; width: 440px; height: 440px;
    border-radius: 50%; background: var(--watermark);
  }
  .offer-brand {
    position: absolute; left: 0; right: 0; top: 118px; text-align: center;
    font-family: "Arimo", sans-serif; font-weight: 700; font-size: 64px;
    color: var(--brand-blue); letter-spacing: -0.5px; line-height: 1;
  }
  .offer-deal {
    position: absolute; left: 0; right: 0; top: 286px; text-align: center;
    font-size: 24px; color: var(--brand-pink); letter-spacing: 0.8px;
  }
  .offer-terms {
    position: absolute; left: 0; right: 0; top: 343px; text-align: center;
    font-size: 40px; letter-spacing: 1.2px;
  }

  /* contact side */
  .brand-mark {
    position: absolute; left: 146px; top: 135px; width: 138px; height: 138px;
    border-radius: 50%; background: var(--brand-blue);
  }
  .brand-name {
    position: absolute; left: 20px; width: 390px; top: 287px; text-align: center;
    font-family: "Arimo", sans-serif; font-weight: 700; font-size: 36px;
    color: var(--brand-blue); line-height: 1;
  }
  .divider {
    position: absolute; left: 427px; top: 87px; width: 1.5px; height: 314px;
    background: var(--brand-blue);
  }
  .contact { position: absolute; left: 457px; top: 98px; }
  .contact__name {
    font-family: "Arimo", sans-serif; font-size: 31px; color: var(--brand-blue);
    line-height: 1; letter-spacing: 0.3px;
  }
  .contact__role { font-size: 22px; line-height: 1; margin-top: 2px; }
  .contact__address { font-size: 23px; line-height: 29px; margin-top: 44px; letter-spacing: 0.5px; }
  .contact__lines { list-style: none; margin-top: 13px; }
  .contact__line { display: flex; align-items: center; height: 27px; font-size: 23px; letter-spacing: 0.5px; }
  .contact__icon { width: 21px; height: 21px; margin-right: 16px; flex: none; }
  .contact__web { font-size: 22px; margin-top: 14px; letter-spacing: 0.5px; }
</style>
</head>
<body>

<section class="card card--offer">
  <div class="offer-watermark"></div>
  <h1 class="offer-brand">KT PRIME MOTION</h1>
  <p class="offer-deal">Show this card to receive 50% off your first 30min pt session</p>
  <p class="offer-terms">Valid to one user only</p>
</section>

<section class="card card--contact">
  <div class="brand-mark"></div>
  <h2 class="brand-name">KT PRIME MOTION</h2>
  <div class="divider"></div>
  <div class="contact">
    <p class="contact__name">EMPLOYEE NAME</p>
    <p class="contact__role">Managing Director</p>
    <p class="contact__address">000 Your address Suite 000<br>FL 00000, Australia</p>
    <ul class="contact__lines">
      <li class="contact__line">
        <svg class="contact__icon" viewBox="0 0 21 21" aria-hidden="true"><rect width="21" height="21" rx="3" fill="#0255a3"/><path d="M7 4.5c.8 0 1.6 2.2 1.6 2.8s-1 .9-1 1.5c.3 1.5 1.6 3.2 3 4 .6.2 1-.8 1.6-.8s2.6 1 2.6 1.7c0 .8-1 2-2 2-3.8 0-7.6-4.6-7.6-8.5 0-1.2 1-2.7 1.8-2.7z" fill="#fff"/></svg>
        +00 000 000 000
      </li>
      <li class="contact__line">
        <svg class="contact__icon" viewBox="0 0 21 21" aria-hidden="true"><rect width="21" height="21" rx="3" fill="#0255a3"/><rect x="6.5" y="4" width="8" height="4" fill="#fff"/><rect x="4" y="8.5" width="13" height="6" rx="1" fill="#fff"/><rect x="6.5" y="12.5" width="8" height="4.5" fill="#fff" stroke="#0255a3" stroke-width="1"/></svg>
        +00 000 000 000
      </li>
      <li class="contact__line">
        <svg class="contact__icon" viewBox="0 0 21 21" aria-hidden="true"><rect width="21" height="21" rx="3" fill="#0255a3"/><rect x="4" y="6" width="13" height="9" fill="#fff"/><path d="M4 6l6.5 5L17 6M4 15l4.5-4.5M17 15l-4.5-4.5" stroke="#0255a3" stroke-width="1" fill="none"/></svg>
        you@yourgmail.com
      </li>
    </ul>
    <p class="contact__web">www.yourcompayweb.com</p>
  </div>
</section>

</body>
</html>
```